Whitcombe Framing Works - Card Design

I am looking to use the logo designs that you already did for me to develop a business card. I would like the card to have a black background and be double sided. I want white and green logo and text. I have attached an inspiration photo of a look that I like. I would like to use the Vertical Logo attached to take up the full front side of the card. On the back where I have my name and information, I would like to have the horizontal logo or maybe even just the image of the 'A' and trees without the text. I am open, but I am looking for something clean and simple and I want the green to really pop! Additional files can be found under Design #: 40593216

Target Market(s)

Homeowners

Industry/Entity Type

Construction

Contact Information for Business Card

Name: Marcus Pellow, Title: Project Manager, Phone: 831.555.0147, Email: whitcombeframingworks@mailbarn.net, address: 418 Juniper Ln, Felton, CA 95092, Lic# 2046318

Colors
00AB8E
00BBA5
67D7C9
C6EFE9
E9F9F6

Requirements
Nice to have
• I would like to see the logos that I have already got from SketchHarbor, though I am open to new ones

```html
<!DOCTYPE html>
<html lang="en">
<head>
<meta charset="utf-8">
<title>Whitcombe Framing Works – Business Card</title>
<link rel="stylesheet" href="https://fonts.googleapis.com/css2?family=Arimo:wght@400;700&display=swap">
<style>
  :root {
    --page: #e4e4e2;
    --card: #2f2f2f;
    --card-deep: #1c1c1c;
    --pattern-mid: #3a3a3a;
    --pattern-light: #5c5c5c;
    --green: #3cb64a;
    --white: #ffffff;
  }
  * { margin: 0; padding: 0; box-sizing: border-box; }
  html, body {
    width: 1200px; height: 801px; overflow: hidden;
    background: var(--page);
    font-family: "Arimo", Arial, sans-serif;
  }
  .sheet {
    width: 1200px; height: 801px;
    display: flex; align-items: center; justify-content: center; gap: 40px;
  }
  .card {
    position: relative;
    width: 540px; height: 309px;
    background: var(--card);
    overflow: hidden;
  }

  /* Contact side */
  .brand-block {
    position: absolute; left: 40px; top: 84px;
    width: 190px; height: 140px;
    display: flex; flex-direction: column; justify-content: center; gap: 10px;
  }
  .brand-square { width: 22px; height: 22px; background: var(--green); }
  .brand-name {
    color: var(--green); font-weight: 700; font-size: 24px; line-height: 1.15;
  }
  .details {
    position: absolute; left: 262px; top: 46px; right: 20px;
    color: var(--white);
  }
  .person-name { color: var(--green); font-weight: 700; font-size: 22px; }
  .person-role { font-size: 14px; margin-top: 4px; }
  .license { font-size: 14px; margin-top: 3px; }
  .license-label { color: var(--green); }
  .contact-list { list-style: none; margin-top: 22px; font-size: 13px; }
  .contact-list li { display: flex; align-items: center; gap: 7px; margin-top: 5px; white-space: nowrap; }
  .contact-icon { width: 12px; height: 12px; flex: none; }
  .address {
    position: absolute; left: 262px; bottom: 40px;
    color: var(--white); font-size: 14px;
  }

  /* Brand side */
  .pattern-field {
    position: absolute; inset: 0;
    background:
      radial-gradient(ellipse 70% 90% at 92% 20%, var(--pattern-light) 0%, transparent 70%),
      radial-gradient(ellipse 60% 70% at 75% 95%, var(--pattern-light) 0%, transparent 65%),
      linear-gradient(30deg, var(--card-deep) 0%, var(--pattern-mid) 55%, var(--pattern-light) 100%);
  }
  .brand-lockup {
    position: absolute; left: 116px; top: 160px;
    display: flex; align-items: center; gap: 12px;
    white-space: nowrap;
  }
  .lockup-square { width: 34px; height: 34px; background: var(--green); flex: none; }
  .lockup-name {
    color: var(--white); font-weight: 700; font-size: 23px; letter-spacing: 0.03em;
  }
</style>
</head>
<body>
<main class="sheet">
  <section class="card card-contact" aria-label="Business card, contact side">
    <div class="brand-block">
      <span class="brand-square"></span>
      <span class="brand-name">Whitcombe Framing Works</span>
    </div>
    <div class="details">
      <p class="person-name">Marcus Pellow</p>
      <p class="person-role">Project Manager</p>
      <p class="license"><span class="license-label">Lic#</span> 2046318</p>
      <ul class="contact-list">
        <li>
          <svg class="contact-icon" viewBox="0 0 12 12" aria-hidden="true">
            <path d="M2.5 1 L4.5 1 L5.2 3.6 L4 4.6 C4.6 6 6 7.4 7.4 8 L8.4 6.8 L11 7.5 L11 9.5 C11 10.3 10.3 11 9.5 11 C5 11 1 7 1 2.5 C1 1.7 1.7 1 2.5 1 Z" fill="none" stroke="#3cb64a" stroke-width="1.1"/>
          </svg>
          831.555.0147
        </li>
        <li>
          <svg class="contact-icon" viewBox="0 0 12 12" aria-hidden="true">
            <rect x="1" y="2.5" width="10" height="7" fill="none" stroke="#3cb64a" stroke-width="1.1"/>
            <path d="M1 2.5 L6 6.5 L11 2.5" fill="none" stroke="#3cb64a" stroke-width="1.1"/>
          </svg>
          whitcombeframingworks@mailbarn.net
        </li>
      </ul>
    </div>
    <p class="address">418 Juniper Ln, Felton, CA 95092</p>
  </section>

  <section class="card card-brand" aria-label="Business card, brand side">
    <div class="pattern-field" role="img" aria-label="Embossed repeating brand pattern covering the card, dark at lower left fading to light grey at upper right"></div>
    <div class="brand-lockup">
      <span class="lockup-square"></span>
      <span class="lockup-name">Whitcombe Framing Works</span>
    </div>
  </section>
</main>
</body>
</html>
```